TN Rovers Brochure Design Project

TN Roves need a brochure to help attract new Tarnello members to our Tarnello club, located in Culpeper, Virginia. The brochure will contain the logo, banner and some pictures provided by me. THe colors and fonts should be consistent throughout. It should include Friendloop, Vidorra Channel and Website information.
The brochure should be able to print in B&W, or color.
I will provide logo, banner, pictures and text in brochure.
You can retrieve PHOTOS and banners from my SNAPLO account:
http://www.snaplo-example.com/photos/bkarnsted/
Target Market(s)
Target customers are "Aircooled and Watercooled Tarnello Enthusiasts" .
Use PHOTOGRAPHS located on my SNAPLO account:
Industry/Entity Type
Club
Requirements
Must have
- I like to have a trifold brochure that will grab your attention immediately.
I will provide the following:
1) Information about our club and how to join
2) Membership Benefits (what will they get out of it?)
3) WEB LINKS - Club Website, Friendloop, and Vidorra Channel
4) Cost to Join
5) Contact information (with email addresses)
6) Our Logo
7) Consistent use of Colors or color scheme
8) Consistent use of fonts
9) Try to incorporate a banner in the brochure somewhere...will provide multiple banners images.
Nice to have
- I have attached some verbiage taken from our TN Rovers website. Some worthsmithing will be required to fit the information into a brochure will be up to you the designer.
I have attached a sample of our TN Membership Application form with membership due information.

```html
<!DOCTYPE html>
<html lang="en">
<head>
<meta charset="utf-8">
<title>TN Rovers – Brochure Panel</title>
<link href="https://fonts.googleapis.com/css2?family=Oswald:wght@600;700&family=Tinos:wght@400;700&display=swap" rel="stylesheet">
<style>
  :root {
    --page: #e3e3e3;
    --navy: #14305a;
    --sky: #4b97e4;
    --gold: #ab9a69;
    --ink: #111111;
    --white: #ffffff;
    --photo-green: #5f8a45;
    --photo-blue: #4d7fae;
    --photo-red: #8c2435;
    --photo-sepia: #9c8c6c;
  }
  * { box-sizing: border-box; margin: 0; padding: 0; }
  html, body { width: 1200px; height: 737px; overflow: hidden; }
  body {
    background: var(--page);
    position: relative;
    font-family: "Tinos", "Times New Roman", serif;
    font-size: 13.6px;
    line-height: 21.4px;
  }
  .block { position: absolute; }
  .heading {
    font-family: "Oswald", "Arial Narrow", sans-serif;
    font-weight: 700;
    font-size: 21px;
    text-transform: uppercase;
    letter-spacing: 0.2px;
  }
  .about-title {
    left: 20px; top: 20px; width: 380px; height: 52px;
    background: var(--navy); color: var(--white);
    padding: 14px 0 0 16px;
  }
  .about-body {
    left: 20px; top: 77px; width: 380px; height: 405px;
    background: var(--navy); color: var(--white);
    padding: 12px 14px 0 16px;
  }
  .event-list { list-style: none; padding-left: 20px; }
  .intro-panel {
    left: 420px; top: 20px; width: 380px; height: 262px;
    background: var(--sky); color: var(--white);
    padding: 12px 14px 0 20px;
    line-height: 21px;
  }
  .intro-panel p { text-indent: 12px; }
  a { color: inherit; text-decoration: underline; }
  .photo { position: absolute; }
  .photo-meadow { left: 20px; top: 498px; width: 380px; height: 216px;
    background: linear-gradient(180deg, #3f5e35 0%, #d8d8d0 30%, #6c8f43 55%, var(--photo-green) 100%); }
  .photo-blue-bus { left: 420px; top: 293px; width: 187px; height: 102px;
    background: linear-gradient(160deg, #7ab4e4 0%, var(--photo-blue) 60%, #3b5f80 100%); }
  .photo-yellow-bus { left: 613px; top: 293px; width: 187px; height: 102px;
    background: linear-gradient(160deg, #6b8a52 0%, #d9a33a 55%, #7b6a4a 100%); }
  .photo-lineup { left: 420px; top: 402px; width: 380px; height: 148px;
    background: linear-gradient(180deg, #3e6a3a 0%, #8fa07a 35%, #8a2f35 55%, #6e7b7a 100%); }
  .photo-red-beetle { left: 820px; top: 20px; width: 358px; height: 245px;
    background: linear-gradient(170deg, #3c5c2e 0%, var(--photo-red) 45%, #5d8a3a 100%); }
  .photo-front-detail { left: 820px; top: 276px; width: 358px; height: 92px;
    background: linear-gradient(90deg, #6f624a 0%, var(--photo-sepia) 50%, #6f624a 100%); }
  .news-title {
    left: 420px; top: 565px; width: 381px; height: 32px;
    color: var(--ink); padding: 0 0 0 11px;
    border-bottom: 3px solid var(--ink);
    font-size: 20px; line-height: 28px;
  }
  .news-body {
    left: 420px; top: 612px; width: 380px;
    color: var(--ink); padding: 0 10px 0 11px;
  }
  .meetings-title {
    left: 820px; top: 377px; width: 358px; height: 48px;
    background: var(--gold); color: var(--white);
    padding: 13px 0 0 18px;
    font-size: 20px;
  }
  .meetings-body {
    left: 820px; top: 432px; width: 358px; height: 282px;
    background: var(--gold); color: var(--white);
    padding: 1px 10px 0 18px;
  }
</style>
</head>
<body>
  <div class="block about-title heading">About Us</div>
  <div class="block about-body">
    <p>The TN Rovers club is based out of Culpeper, Virginia, and is dedicated to the preservation of custom and stock TNs, both water and air-cooled varieties.&nbsp; Our club is a place to connect with other TN enthusiasts whether it is to cruise, attend shows, share project ideas/tips, or simply share the love of the TN.&nbsp; Members are very active and take great pride in their Tarnellos. Our group meets monthly and sponsors the following events during the year.</p>
    <ul class="event-list">
      <li>Annual Show at the Skyfield Air Show in Bealeton,<br>VA-1st weekend in May</li>
      <li>Summer Picnic and Cruise</li>
      <li>Fall Cruise to Skyline Drive</li>
      <li>Member Christmas Party</li>
    </ul>
    <p>In between these club activities we cruise in support of our neighboring Tarnello clubs and up and down the east coast. Please visit our CALENDAR page for list of upcoming events. We also post events on our TN Rovers - Virginia Friendloop page, so please join us there also.</p>
  </div>

  <div class="photo photo-meadow" role="img" aria-label="Photo of classic cars and canopies at an outdoor club show on a grassy field"></div>

  <div class="block intro-panel">
    <p>Our club was formed in 2001, and the club is excited about planning new events that everyone can enjoy throughout the year. We also have a handful of TN experts that can provide tips on repairing or restoring your TN. Club membership benefits allow you to search through our online discussion forum called "RoverDen", for Tech tips or any general discussion related to TNs.</p>
    <p>All water and air-cooled TN enthusiasts are welcome to join. For more information about who we are and what we do, browse this site <a href="#">TNRovers-Virginia.com</a> , stop by a meeting or event, or get in touch with us via our CONTACT page.</p>
  </div>

  <div class="photo photo-blue-bus" role="img" aria-label="Photo of a blue lettered vintage van"></div>
  <div class="photo photo-yellow-bus" role="img" aria-label="Photo of a yellow and white vintage van"></div>
  <div class="photo photo-lineup" role="img" aria-label="Photo of classic cars and a red pickup lined up at a show"></div>

  <div class="block news-title heading">News/Events</div>
  <div class="block news-body">
    <p>Get the latest news on upcoming club activities by visiting our CALENDAR page. We also share pictures and discuss our projects and activities on our Open Friendloop Group page <a href="#">TNRovers - Virginia</a>, so please be sure to look us up there.</p>
  </div>

  <div class="photo photo-red-beetle" role="img" aria-label="Photo of a red classic car with open engine lid on grass"></div>
  <div class="photo photo-front-detail" role="img" aria-label="Sepia close-up photo of a classic car front with headlights"></div>

  <div class="block meetings-title heading">Monthly Membership Meetings</div>
  <div class="block meetings-body">
    <p>Our monthly club membership meetings take place on the third Thursday night of every month at Marlo's Restaurant, located in Culpeper, VA. We start the meeting at 7:00 p.m., however, if you wish to eat before the meeting, we recommend you arrive around 6:30 p.m. Visit our Monthly Meetings page to find out more.<br>Visit Marlo's on MapFinder for directions.<br>If you are interested in becoming a member of our TN club or want to review the benefits of membership, please visit our Join Us webpage, for more details on membership. You don't need to own a TN to belong to this club. <a href="#">Membership dues are $ 25 for individual and $ 35 for families.&nbsp;</a></p>
  </div>
</body>
</html>
```